Criação de Papelaria (6 itens) para Brisa & Coral
" Serviços Exclusivos p/ Receptivo Turistico. Aluguel de Carros e Motos - Roteiros - Transfers - Reservas e Enxovais "

```html
<!DOCTYPE html>
<html lang="pt-BR">
<head>
<meta charset="UTF-8">
<title>Brisa &amp; Coral — Cartão de Visita</title>
<link href="https://fonts.googleapis.com/css2?family=Didact+Gothic&display=swap" rel="stylesheet">
<style>
  :root {
    --page-bg: #ecebe8;
    --card-dark: #353537;
    --card-dark-edge: #2a2a2c;
    --card-light: #ffffff;
    --gold: #b8895a;
    --ink: #2f2f31;
    --ink-soft: #4a4a4d;
  }
  * { margin: 0; padding: 0; box-sizing: border-box; }
  html, body {
    width: 1200px; height: 1200px; overflow: hidden;
    background: var(--page-bg);
    font-family: "Didact Gothic", sans-serif;
  }
  .stage {
    width: 1200px; height: 1200px;
    display: flex; flex-direction: column;
    align-items: center; justify-content: center;
    gap: 60px;
  }
  .card {
    width: 880px; height: 489px;
    border-radius: 26px;
    position: relative;
    box-shadow: 0 10px 30px rgba(0,0,0,0.12);
  }
  .card-front {
    background: linear-gradient(135deg, var(--card-dark) 0%, var(--card-dark-edge) 100%);
    display: flex; align-items: center; justify-content: center;
  }
  .brand {
    display: flex; align-items: center; gap: 20px;
    color: var(--gold);
    font-size: 64px;
    letter-spacing: 2px;
    white-space: nowrap;
  }
  .brand-dot {
    width: 18px; height: 18px; border-radius: 50%;
    background: var(--gold);
  }
  .brand-small { font-size: 46px; gap: 14px; letter-spacing: 1px; }
  .brand-small .brand-dot { width: 13px; height: 13px; }

  .card-back { background: var(--card-light); color: var(--ink); }
  .identity {
    position: absolute; left: 64px; top: 56px;
  }
  .person-name { font-size: 40px; line-height: 1.15; }
  .person-role { font-size: 36px; line-height: 1.15; color: var(--ink-soft); }
  .contact-list {
    list-style: none;
    font-size: 19px; line-height: 1.55; color: var(--ink-soft);
  }
  .contact-list .label { display: inline-block; width: 88px; }
  .contact-mobile { margin-top: 22px; }
  .contact-office { position: absolute; left: 64px; bottom: 56px; }
  .card-back .brand { position: absolute; right: 70px; top: 232px; }
</style>
</head>
<body>
<main class="stage">
  <section class="card card-front" aria-label="Frente do cartão">
    <div class="brand"><span class="brand-dot"></span><span class="brand-name">Brisa &amp; Coral</span></div>
  </section>

  <section class="card card-back" aria-label="Verso do cartão">
    <div class="identity">
      <p class="person-name">Nome Completo</p>
      <p class="person-role">Cargo/Função</p>
      <ul class="contact-list contact-mobile">
        <li><span class="label">Mobile</span>(73) 9876-5432</li>
        <li><span class="label">e-mail</span>contato@brisaecoral.com</li>
      </ul>
    </div>

    <ul class="contact-list contact-office">
      <li><span class="label">Phone</span>(73) 3288-1040</li>
      <li><span class="label">Address</span>Rua das Gaivotas, 240</li>
      <li><span class="label">Conj</span>Sala 12 - Porto Seguro - 45810-000</li>
      <li><span class="label">Website</span>www.brisaecoral.com.br</li>
    </ul>

    <div class="brand brand-small"><span class="brand-dot"></span><span class="brand-name">Brisa &amp; Coral</span></div>
  </section>
</main>
</body>
</html>
```